Sharper Daily Habits Qorafone App

I am looking to create an Qorafone app (support Qorafone 5 and above) that will inspire and empower the app user to be more productive through a creative, interative and simplistic user experience that teaches the 10 topics related to "Sharper Daily Habits". Please see attached zip files for the 10 topic as PDF files and 20 posters (20 jpg files) which include a quote related to the content bundle’s topic.

Target Market(s)

working professionals who desire to be more productive in their ways of doing

Industry/Entity Type

It Support

Font styles to use
Sans Serif

Colors
33a6d7
0255a3
9bcb3b
cadf82
33b8a4

Requirements
Must have
• don't really wanna say "ebook" style app which would be below my expectation, i expect something more creative than an "ebook" app. i prefer you use your creativity to come up with the design but if you are a bit lost, please read below.
• some specs in my mind:
• - 10 flash cards design for each of the topic so they can be used in a carousel style menu (see sample app screenshot 1 - 1st screen to the left)
• - when presenting a topic, the background should be the same as the flash card of the topic (see sample app screenshot 2 - the right most screen)
• - at the bottom of the topic screen, a audio play/pause buttons bar should be presented as the app will play audible version for the article.
• - the fashion of the sample app screen shots shouldn't be followed as it is an ancient fashion reflecting the content. I expect the fashion of the app should be modern and reflect the topic "sharper daily habits"
• Screens required:
• - Main menu screen: carosoul style presenting the 10 topics using flash cards, should have a "play/pause" button to play the audible topic
• - Topic screen: presents the text content of the topic with flash card design as the background, paging buttons when content spans over one page, have media player bar at bottom to "play/pause/fast forward/reverse" audible
Nice to have
• i have 20 posters with quotes that inspires the user. i would like to see the posters to be presented full screen with a "inspire me" button somewhere which will randomly display a poster to the user.

```html
<!DOCTYPE html>
<html lang="en">
<head>
<meta charset="utf-8">
<title>Sharper Daily Habits – App Screens</title>
<link rel="stylesheet" href="https://fonts.googleapis.com/css2?family=Arimo:wght@400;700&family=Crimson+Pro:wght@400;700&display=swap">
<style>
:root{
  --stage:#7a958c;
  --teal:#33b8a4;
  --teal-dark:#2aa894;
  --white:#ffffff;
  --ink:#1d1d1d;
  --ink-soft:#2f2f2f;
  --note:#e8334a;
  --track:#d9d9d9;
}
*{box-sizing:border-box;margin:0;padding:0}
html,body{width:699px;height:1200px;overflow:hidden;background:var(--stage)}
body{position:relative;font-family:"Arimo",Helvetica,Arial,sans-serif;color:var(--ink)}
.screen{position:absolute;width:320px;height:568px;overflow:hidden;
  background:
   radial-gradient(circle at 20% 15%,#f6c9d2 0,transparent 40%),
   radial-gradient(circle at 85% 30%,#f2d6e0 0,transparent 40%),
   radial-gradient(circle at 30% 80%,#f3ecb9 0,transparent 45%),
   radial-gradient(circle at 80% 85%,#cfe8ef 0,transparent 45%),
   #ece3e6;}
.screen--grid{left:20px;top:20px}
.screen--carousel{left:359px;top:20px}
.screen--reader{left:190px;top:612px}
.status-bar{position:absolute;top:0;left:0;right:0;height:20px;background:var(--white);
  font-size:12px;display:flex;align-items:center;justify-content:space-between;padding:0 6px}
.status-bar .carrier{display:flex;align-items:center;gap:3px}
.status-bar .time{position:absolute;left:0;right:0;text-align:center}
.status-bar .battery{display:flex;align-items:center;gap:3px}
.battery-icon{width:24px;height:11px;border:1px solid #222;border-radius:2px;padding:1px}
.battery-icon span{display:block;height:100%;background:#222}
.app-header{position:absolute;top:20px;left:0;right:0;height:84px;background:var(--white)}
.menu-icon{position:absolute;left:15px;top:14px}
.app-title{position:absolute;left:70px;top:12px;font-size:18px;font-weight:700;letter-spacing:.1px}
.view-toggle{position:absolute;left:84px;top:43px;width:152px;height:28px;border:1.5px solid var(--teal);border-radius:4px;display:flex;overflow:hidden}
.view-toggle span{flex:1;display:flex;align-items:center;justify-content:center}
.view-toggle .active{background:var(--teal)}
.audio-bar{position:absolute;left:0;right:0;bottom:0;height:43px;background:var(--white);display:flex;align-items:center;padding:0 14px}
.audio-bar .label{margin-left:16px;font-size:16px}
.switch{margin-left:auto;width:52px;height:31px;border-radius:16px;background:var(--teal);position:relative}
.switch::after{content:"";position:absolute;right:2px;top:2px;width:27px;height:27px;border-radius:50%;background:var(--white);box-shadow:0 1px 3px rgba(0,0,0,.3)}
.poster{position:absolute;border-radius:3px;box-shadow:0 1px 3px rgba(0,0,0,.35)}
.p1{background:linear-gradient(160deg,#f3e3c3 0,#c23b36 55%,#3a2c2a 100%)}
.p2{background:linear-gradient(160deg,#f1e4c4 0,#e8c43e 50%,#7d3a2f 100%)}
.p3{background:linear-gradient(160deg,#e0323c 0,#f3d43b 50%,#2fb7c5 100%)}
.p4{background:linear-gradient(160deg,#f0e2c0 0,#3a9da0 50%,#2a2a2a 100%)}
.p5{background:linear-gradient(160deg,#f2c9a0 0,#4aa6a6 55%,#263238 100%)}
.p6{background:linear-gradient(160deg,#e6c14a 0,#d24b3e 50%,#2a2a2a 100%)}
.p7{background:linear-gradient(160deg,#53c2b4 0,#f3e8c8 55%,#c73a34 100%)}
.p8{background:linear-gradient(160deg,#45b8b0 0,#c73a3a 50%,#e9c742 100%)}
.p9{background:linear-gradient(160deg,#e33b3b 0,#f1e6c4 50%,#3aa7a0 100%)}
.card-caption{position:absolute;width:100px;text-align:center;font-size:12px;line-height:14px}
.carousel-title{position:absolute;left:0;right:0;top:402px;text-align:center;font-size:16.5px;font-weight:700;line-height:20px}
.carousel-count{position:absolute;left:0;right:0;top:464px;text-align:center;font-size:16px;font-weight:700}
.side{position:absolute;box-shadow:0 2px 6px rgba(0,0,0,.35)}
.reader-title{position:absolute;left:0;right:0;top:32px;text-align:center;font-family:"Crimson Pro",Georgia,serif;font-weight:700;font-size:17px;line-height:20.5px}
.back{position:absolute;left:8px;top:32px}
.reader-body{position:absolute;left:17px;right:14px;top:108px;font-family:"Crimson Pro",Georgia,serif;font-size:17.2px;line-height:24.9px;color:var(--ink-soft)}
.reader-body p{text-indent:10px;margin-bottom:24.9px}
.player-bar{position:absolute;left:0;right:0;bottom:0;height:44px;background:var(--white);display:flex;align-items:center;justify-content:space-between;padding:0 20px}
.text-size{color:var(--teal);font-size:11px;letter-spacing:-.5px}
.text-size b{font-size:13px;font-weight:400}
.text-size i{font-style:normal;font-size:16px}
</style>
</head>
<body>

<!-- Grid menu -->
<section class="screen screen--grid">
  <div class="status-bar">
    <span class="carrier">●●●○○ Vantel
      <svg width="12" height="9" viewBox="0 0 12 9"><path d="M6 9 0 3a8.5 8.5 0 0 1 12 0z" fill="#222"/></svg></span>
    <span class="time">4:21 PM</span>
    <span class="battery">100% <span class="battery-icon"><span></span></span></span>
  </div>
  <header class="app-header">
    <svg class="menu-icon" width="26" height="18" viewBox="0 0 26 18"><g fill="#33b8a4"><rect width="26" height="2.6"/><rect y="7.7" width="26" height="2.6"/><rect y="15.4" width="26" height="2.6"/></g></svg>
    <h1 class="app-title">Sharper Daily Habits</h1>
    <div class="view-toggle">
      <span class="active"><svg width="16" height="16" viewBox="0 0 16 16" fill="#fff"><rect width="4" height="4"/><rect x="6" width="4" height="4"/><rect x="12" width="4" height="4"/><rect y="6" width="4" height="4"/><rect x="6" y="6" width="4" height="4"/><rect x="12" y="6" width="4" height="4"/><rect y="12" width="4" height="4"/><rect x="6" y="12" width="4" height="4"/><rect x="12" y="12" width="4" height="4"/></svg></span>
      <span><svg width="20" height="16" viewBox="0 0 20 16" fill="#33b8a4"><rect x="5" width="10" height="16"/><rect y="3" width="3" height="10"/><rect x="17" y="3" width="3" height="10"/></svg></span>
    </div>
  </header>

  <div class="poster p1" role="img" aria-label="Topic poster with typographic quote" style="left:25px;top:125px;width:66px;height:84px"></div>
  <div class="poster p2" role="img" aria-label="Topic poster with typographic quote" style="left:127px;top:125px;width:66px;height:84px"></div>
  <div class="poster p3" role="img" aria-label="Topic poster with typographic quote" style="left:228px;top:125px;width:66px;height:84px"></div>
  <p class="card-caption" style="left:8px;top:214px">An Introduction to Highly Pro...</p>
  <p class="card-caption" style="left:110px;top:214px">How to Avoid Distractions</p>
  <p class="card-caption" style="left:211px;top:214px">How to Have the Most Pro...</p>

  <div class="poster p4" role="img" aria-label="Topic poster with typographic quote" style="left:25px;top:256px;width:66px;height:84px"></div>
  <div class="poster p5" role="img" aria-label="Topic poster with typographic quote" style="left:127px;top:256px;width:66px;height:84px"></div>
  <div class="poster p6" role="img" aria-label="Topic poster with typographic quote" style="left:228px;top:256px;width:66px;height:84px"></div>
  <p class="card-caption" style="left:8px;top:344px">How to Speed Up Your Typi...</p>
  <p class="card-caption" style="left:110px;top:344px">How to Spend Less Time on...</p>
  <p class="card-caption" style="left:211px;top:344px">Incentivizing Productivity vs...</p>

  <div class="poster p7" role="img" aria-label="Topic poster with typographic quote" style="left:25px;top:390px;width:66px;height:84px"></div>
  <div class="poster p8" role="img" aria-label="Topic poster with typographic quote" style="left:127px;top:390px;width:66px;height:84px"></div>
  <div class="poster p9" role="img" aria-label="Topic poster with typographic quote" style="left:228px;top:390px;width:66px;height:84px"></div>
  <p class="card-caption" style="left:8px;top:479px">Productivity is Happiness</p>
  <p class="card-caption" style="left:110px;top:479px">Try This One Smart Trick to...</p>
  <p class="card-caption" style="left:211px;top:479px">Why Nutrition and Producti...</p>

  <div class="audio-bar">
    <svg width="22" height="26" viewBox="0 0 22 26"><path d="M7 3 21 0v18a4 4 0 1 1-2-3.4V5L9 7v14a4 4 0 1 1-2-3.4z" fill="#e8334a"/></svg>
    <span class="label">Audio Background</span>
    <span class="switch"></span>
  </div>
</section>

<!-- Carousel menu -->
<section class="screen screen--carousel">
  <div class="status-bar">
    <span class="carrier">●●●○○ Vantel
      <svg width="12" height="9" viewBox="0 0 12 9"><path d="M6 9 0 3a8.5 8.5 0 0 1 12 0z" fill="#222"/></svg></span>
    <span class="time">4:21 PM</span>
    <span class="battery">100% <span class="battery-icon"><span></span></span></span>
  </div>
  <header class="app-header">
    <svg class="menu-icon" width="26" height="18" viewBox="0 0 26 18"><g fill="#33b8a4"><rect width="26" height="2.6"/><rect y="7.7" width="26" height="2.6"/><rect y="15.4" width="26" height="2.6"/></g></svg>
    <h1 class="app-title">Sharper Daily Habits</h1>
    <div class="view-toggle">
      <span><svg width="16" height="16" viewBox="0 0 16 16" fill="#33b8a4"><rect width="4" height="4"/><rect x="6" width="4" height="4"/><rect x="12" width="4" height="4"/><rect y="6" width="4" height="4"/><rect x="6" y="6" width="4" height="4"/><rect x="12" y="6" width="4" height="4"/><rect y="12" width="4" height="4"/><rect x="6" y="12" width="4" height="4"/><rect x="12" y="12" width="4" height="4"/></svg></span>
      <span class="active"><svg width="20" height="16" viewBox="0 0 20 16" fill="#fff"><rect x="5" width="10" height="16"/><rect y="3" width="3" height="10"/><rect x="17" y="3" width="3" height="10"/></svg></span>
    </div>
  </header>

  <div class="side p4" role="img" aria-label="Previous topic poster, angled" style="left:10px;top:170px;width:58px;height:200px;clip-path:polygon(0 0,100% 9%,100% 91%,0 100%)"></div>
  <div class="poster p3" role="img" aria-label="Current topic poster with typographic quote" style="left:75px;top:163px;width:169px;height:230px;border-radius:0"></div>
  <div class="side p7" role="img" aria-label="Next topic poster, angled" style="left:252px;top:170px;width:58px;height:200px;clip-path:polygon(0 9%,100% 0,100% 100%,0 91%)"></div>

  <p class="carousel-title">How to Have the Most Productive Day<br>Possible Using Hacks</p>
  <p class="carousel-count">(3 of 10)</p>

  <div class="audio-bar">
    <svg width="22" height="26" viewBox="0 0 22 26"><path d="M7 3 21 0v18a4 4 0 1 1-2-3.4V5L9 7v14a4 4 0 1 1-2-3.4z" fill="#e8334a"/></svg>
    <span class="label">Audio Background</span>
    <span class="switch"></span>
  </div>
</section>

<!-- Topic reader -->
<section class="screen screen--reader">
  <div class="status-bar">
    <span class="carrier">●●●○○ Vantel
      <svg width="12" height="9" viewBox="0 0 12 9"><path d="M6 9 0 3a8.5 8.5 0 0 1 12 0z" fill="#222"/></svg></span>
    <span class="time">4:21 PM</span>
    <span class="battery">100% <span class="battery-icon"><span></span></span></span>
  </div>
  <svg class="back" width="14" height="22" viewBox="0 0 14 22"><path d="M12 2 3 11l9 9" fill="none" stroke="#33b8a4" stroke-width="2.6"/></svg>
  <h2 class="reader-title">How to Have the Most<br>Productive Day Possible<br>Using Hacks</h2>
  <div class="reader-body">
    <p>If you read the advice of productivity gurus then &nbsp;you will &nbsp;find they often give tips and advice on ways that you can increase your output and productivity through clever lifestyle hacks. These include little changes to your routine and workflow that help to make you more engaged, less distracted and more full of energy.</p>
    <p>On their own, these tips and hacks tend to have only a minor impact. But what if you try them all at once? Then you would get a cumulative effect that should drastically increase your productivity.</p>
  </div>
  <nav class="player-bar">
    <svg width="12" height="18" viewBox="0 0 12 18"><path d="M10 2 3 9l7 7" fill="none" stroke="#33b8a4" stroke-width="2.4"/></svg>
    <span class="text-size">A<b>A</b><i>A</i></span>
    <svg width="18" height="22" viewBox="0 0 18 22" fill="#33b8a4"><rect width="6" height="22"/><rect x="12" width="6" height="22"/></svg>
    <span style="width:24px"></span>
    <svg width="12" height="18" viewBox="0 0 12 18"><path d="M2 2l7 7-7 7" fill="none" stroke="#33b8a4" stroke-width="2.4"/></svg>
  </nav>
</section>

</body>
</html>
```